Packaging Design for Fruit Juice Product

The Product is a fruit juice product. Kindly refer to the photograph attached for the temporary bottle shape and label position. (Please note that the cap colour will be different (not green), as it will be adjusted with the label design)

The fruit is Carica (it's similar like Papaya, but just in yellow color and smaller size). Like the other juice products, the target market covers most of the age range from 10 - 60 years old.

The temporary product name is: KEM

The fact that this juice product is quite unique, I want the product design to be something revolutionary and 'epic'.
The graphic design could be anything depends on your imagination. Basically, I want you to expand your creativity in designing the logo and the overall graphic design for the label.

- Do not design something ordinary or mediocre. Be Extraordinary -

*****The information below may / may not be used to base the label design. It is all up to you to decide whether it is useful in designing the label or not*****

I also have attached the basic information of the fruit and the place where the Carica tree grows: Dieng Plateau.
Dieng Plateau is Highland area where there are mountains. This Dieng Plateau is believed to be the place where the Gods live in the past.
This is probably because of the beautiful landscapes and the epic nature gift such as multi colour lakes, Volcanic crater, etc. (There are lots of myth about this place anyway).
Updates

There are lots of amazing and absolutely great designs on these websites:
You may want to check for the inspiration of our Fruit Juice Project 

Industry/Entity Type

Graphic Design

Requirements
Must have
• Remarkable logo and graphic design.

```html
<!DOCTYPE html>
<html lang="en">
<head>
<meta charset="utf-8">
<title>KEM Carica Juice – Label</title>
<link href="https://fonts.googleapis.com/css2?family=Marcellus&family=Archivo:wght@700&family=Tinos&display=swap" rel="stylesheet">
<style>
  :root {
    --paper: #ffffff;
    --ink: #231f20;
    --orange: #f26a1b;
    --orange-light: #f9a23b;
    --papaya-skin: #e9b54a;
    --frame: #231f20;
  }
  html, body {
    margin: 0;
    padding: 0;
    width: 1200px;
    height: 1000px;
    overflow: hidden;
    background: var(--paper);
  }
  .canvas {
    position: relative;
    width: 1200px;
    height: 1000px;
  }
  .label {
    position: absolute;
    left: 340px;
    top: 25px;
    width: 520px;
    height: 950px;
    box-sizing: border-box;
    border: 2px solid var(--frame);
    background: var(--paper);
  }
  .brand {
    position: absolute;
    top: 55px;
    left: 0;
    width: 100%;
    display: flex;
    justify-content: center;
    align-items: center;
    gap: 14px;
  }
  .brand-name {
    font-family: "Marcellus", serif;
    font-size: 130px;
    line-height: 1;
    color: var(--orange);
    letter-spacing: 2px;
  }
  .brand-dot {
    width: 72px;
    height: 72px;
    border-radius: 50%;
    background: var(--orange);
  }
  .product-line {
    position: absolute;
    left: 0;
    width: 100%;
    text-align: center;
    font-family: "Marcellus", serif;
    line-height: 1;
  }
  .product-line.fruit {
    top: 196px;
    font-size: 46px;
    letter-spacing: 14px;
    color: var(--ink);
    padding-left: 14px;
    box-sizing: border-box;
  }
  .product-line.kind {
    top: 248px;
    font-size: 48px;
    letter-spacing: 16px;
    color: var(--orange);
    padding-left: 16px;
    box-sizing: border-box;
  }
  .claim-band {
    position: absolute;
    top: 350px;
    left: 47px;
    width: 438px;
    height: 41px;
    border-radius: 4px;
    background: var(--ink);
    color: var(--paper);
    font-family: "Archivo", sans-serif;
    font-weight: 700;
    font-size: 24px;
    letter-spacing: 1px;
    word-spacing: 14px;
    display: flex;
    align-items: center;
    justify-content: center;
  }
  .fruit-photo {
    position: absolute;
    top: 495px;
    left: 85px;
    width: 350px;
    height: 240px;
    border-radius: 48% 52% 46% 54% / 55% 50% 50% 45%;
    background: radial-gradient(ellipse at 55% 60%, var(--orange) 0%, #f47c22 45%, var(--papaya-skin) 80%, rgba(233,181,74,0) 100%);
  }
  .origin {
    position: absolute;
    top: 818px;
    left: 0;
    width: 100%;
    text-align: center;
    font-family: "Marcellus", serif;
    font-size: 27px;
    line-height: 31px;
    letter-spacing: 9px;
    color: var(--ink);
    padding-left: 9px;
    box-sizing: border-box;
  }
  .volume {
    position: absolute;
    top: 893px;
    left: 0;
    width: 100%;
    text-align: center;
    font-family: "Tinos", serif;
    font-size: 20px;
    color: var(--ink);
  }
</style>
</head>
<body>
<div class="canvas">
  <div class="label">
    <div class="brand">
      <span class="brand-name">KEM</span>
      <span class="brand-dot"></span>
    </div>
    <div class="product-line fruit">CARICA</div>
    <div class="product-line kind">JUICE</div>
    <div class="claim-band">PREMIUM FRESH QUALITY</div>
    <div class="fruit-photo" role="img" aria-label="Photo of a whole carica fruit behind a halved carica showing orange flesh and black seeds"></div>
    <div class="origin">PRODUCT OF<br>DIENG PLATEAU</div>
    <div class="volume">250 ml</div>
  </div>
</div>
</body>
</html>
```